Real Estate Managemene Company Needs Business Card Design

We have a logo design and just need business cards made now for our business. Please use PDF logo # 3.

Card with Information to be attached shortly.

The card is used for a real estate management company. We will need to add four other employees and their cards.

Industry/Entity Type

Real Estate

Contact Information for Business Card

Tariq Hamdan
President
3187 Thornwick Avenue
Suite C
Maple Hollow, WI 60152
Phone 630.417.2286
Fax 630.417.2287
Cell 630.473.8062
vantorp@mailbreeze.net

Once design is approved we will have four other employees
Omar Hamdan
Operations Manager

Nadia Hamdan
Administrative Manager

Faz Hamdan
Principal

We would need to take out the cell # 630.473.8062 out for the remaining three cards.

Requirements
Must have
• Please use logo attached

```html
<!DOCTYPE html>
<html lang="en">
<head>
<meta charset="utf-8">
<title>Crestfield Property Management Group – Business Card</title>
<link rel="stylesheet" href="https://fonts.googleapis.com/css2?family=Roboto:wght@400;700&display=swap">
<style>
  :root {
    --page: #ecebe8;
    --brand-blue: #1f5c9c;
    --brand-blue-dark: #174a80;
    --brand-blue-light: #3b7cc0;
    --ink: #1e1e1e;
    --muted: #5a5a5a;
    --charcoal: #2f2f31;
    --paper: #ffffff;
    --divider: #e2e2e2;
  }
  * { box-sizing: border-box; margin: 0; padding: 0; }
  html, body { width: 1200px; height: 950px; overflow: hidden; }
  body {
    background: var(--page);
    font-family: "Roboto", Arial, sans-serif;
    position: relative;
  }
  .card {
    position: absolute;
    left: 240px;
    width: 720px;
    height: 411px;
    border-radius: 4px;
    overflow: hidden;
    box-shadow: 0 6px 18px rgba(0,0,0,0.18);
  }
  .card--front { top: 44px; background: linear-gradient(160deg, var(--brand-blue-light) 0%, var(--brand-blue) 45%, var(--brand-blue-dark) 100%); }
  .card--back { top: 495px; background: var(--paper); }

  .wordmark { display: flex; align-items: center; gap: 14px; font-weight: 700; letter-spacing: 1px; line-height: 1.15; }
  .wordmark__square { width: 22px; height: 22px; flex: none; }
  .wordmark__name { font-size: 26px; text-transform: uppercase; white-space: nowrap; }
  .wordmark__name small { display: block; font-size: 13px; letter-spacing: 2px; }

  .card--front .wordmark { position: absolute; left: 50%; top: 50%; transform: translate(-50%, -50%); color: #fff; }
  .card--front .wordmark__square { background: #fff; }

  .card--back .wordmark { position: absolute; left: 46px; top: 168px; color: var(--ink); }
  .card--back .wordmark__square { background: var(--brand-blue); }
  .card--back .wordmark__name { font-size: 22px; }
  .card--back .wordmark__name small { font-size: 11px; }

  .divider {
    position: absolute; left: 408px; top: 24px; width: 1px; height: 300px;
    background: var(--divider);
    box-shadow: 2px 0 6px rgba(0,0,0,0.06);
  }
  .contact { position: absolute; left: 436px; top: 40px; color: var(--muted); font-size: 16px; line-height: 1.35; }
  .contact__name { color: var(--brand-blue); font-size: 23px; font-weight: 700; }
  .contact__title { color: var(--ink); font-size: 16px; margin-bottom: 6px; }
  .contact__lines { list-style: none; margin-top: 6px; }
  .contact__lines li { display: flex; align-items: center; gap: 8px; }
  .contact__lines svg { width: 15px; height: 15px; fill: var(--brand-blue); flex: none; }

  .band { position: absolute; }
  .band--blue { left: 0; bottom: 0; width: 530px; height: 26px; background: linear-gradient(90deg, var(--brand-blue-dark), var(--brand-blue-light)); }
  .band--blue-fade { left: 0; bottom: 26px; width: 530px; height: 18px; background: linear-gradient(180deg, rgba(59,124,192,0), rgba(59,124,192,0.25)); }
  .band--charcoal { right: 0; bottom: 0; width: 190px; height: 58px; background: var(--charcoal); }
  .band--accent { left: 530px; bottom: 0; width: 6px; height: 58px; background: var(--brand-blue-light); }
</style>
</head>
<body>

<section class="card card--front" aria-label="Card front">
  <div class="wordmark">
    <span class="wordmark__square"></span>
    <span class="wordmark__name">Crestfield<small>Property Management Group</small></span>
  </div>
</section>

<section class="card card--back" aria-label="Card back">
  <div class="wordmark">
    <span class="wordmark__square"></span>
    <span class="wordmark__name">Crestfield<small>Property Management Group</small></span>
  </div>

  <div class="divider"></div>

  <div class="contact">
    <p class="contact__name">Tariq Hamdan</p>
    <p class="contact__title">President</p>
    <p>3187 Thornwick Avenue</p>
    <p>Suite C</p>
    <p>Maple Hollow, WI 60152</p>
    <ul class="contact__lines">
      <li><svg viewBox="0 0 16 16" aria-label="Phone"><path d="M3 1h3l1.5 4-2 1.3a9 9 0 0 0 4.2 4.2L11 8.5 15 10v3a2 2 0 0 1-2 2A12 12 0 0 1 1 3a2 2 0 0 1 2-2z"/></svg>630.417.2286</li>
      <li><svg viewBox="0 0 16 16" aria-label="Mobile"><path d="M4 0h8a1 1 0 0 1 1 1v14a1 1 0 0 1-1 1H4a1 1 0 0 1-1-1V1a1 1 0 0 1 1-1zm1 2v10h6V2zm3 11a1 1 0 1 0 0 2 1 1 0 0 0 0-2z"/></svg>630.473.8062</li>
      <li><svg viewBox="0 0 16 16" aria-label="Fax"><path d="M4 1h8v4H4zM1 6h14v7h-3v2H4v-2H1zm4 5v3h6v-3z"/></svg>630.417.2287</li>
      <li><svg viewBox="0 0 16 16" aria-label="Email"><path d="M1 3h14v10H1zm1.5 1.2L8 8.5l5.5-4.3z"/></svg>vantorp@mailbreeze.net</li>
    </ul>
  </div>

  <div class="band band--blue-fade"></div>
  <div class="band band--blue"></div>
  <div class="band band--accent"></div>
  <div class="band band--charcoal"></div>
</section>

</body>
</html>
```